R&T Cleanwave Stripping Business Card

We are in need of a business card design for our new Texas based company called 'R&T Cleanwave Stripping'. Our new innovative mobile media blasting service utilizes recycled material and a new water based process that eliminates all dust (i.e. as apposed to the old sand blasting format). Our 'advanced surface preparation' service targets multiple industries such as automotive, Industrial, marine and structural (graffiti removal). We would like to see the design include a recycling type logo or concept that utilizes colors such as black, various shades of green, some white, yellow and/or grey (e.g. perhaps a blackish background). The final design should look simple and professional and should clearly communicate the environmentally friendly approach through logo or design (i.e. Eco-Friendly, Go Green or Blast Green methodologies). Thank you in advance!
Updates

Please pardon any inconvenience. We have decided to pursue a two sided business card. All original information/designs requirements remains the same for the front. However, we would like back of the card to state the following: "We bring the power of Hydroveil Media Scouring equipment to your location. We can remove any coating from any surface. Bullets include: Paint Stripping, Auto Restoration, Graffiti Removal, Black Walls & Stone, Concrete, Boats, Iron Fences, Tractors & Trailers, Pools & Fountains, Wood Restoration.

Industry/Entity Type

Recycling

Contact Information for Business Card

R&T Cleanwave Stripping, LLC - Gordon Pelly, MBA, PMP - cell: 915-382-6091, office: 915-627-8853 - gpelly@rtcleanwavestripping.com - CEO/Founder

Requirements
Must have
• Recycle or environmentally friendly logos or design.
Nice to have
• Business oriented design with an aggressive look. Also, if possible would like to see R&T incorporated into the design or logo. Please note that we have decided to add the option of adding details to the back of the card (2 sided). The front should contain the logo/design and the back should have the following details listed: "We bring the power of Hydroveil Media Scouring equipment to your location. We can remove any coating from any surface. Bullets include: Paint Stripping, Auto Restoration, Graffiti Removal, Black Walls & Stone, Concrete, Boats, Iron Fences, Tractors & Trailers, Pools & Fountains, Wood Restoration.

```html
<!DOCTYPE html>
<html lang="en">
<head>
<meta charset="utf-8">
<title>R&amp;T Cleanwave Stripping – Business Card</title>
<link href="https://fonts.googleapis.com/css2?family=Questrial&display=swap" rel="stylesheet">
<style>
  :root {
    --backdrop: #4b423c;
    --card-black: #1c1c1c;
    --card-black-deep: #141414;
    --paper-white: #f4f4f4;
    --paper-grey: #dcdcdc;
    --brand-green: #1e9a3c;
    --text-green: #2fae4a;
    --text-white: #f2f2f2;
    --ghost-grey: #2c2c2c;
    --divider: #3a3a3a;
  }
  * { margin: 0; padding: 0; box-sizing: border-box; }
  html, body { width: 1200px; height: 827px; overflow: hidden; }
  body {
    background: var(--backdrop);
    font-family: "Questrial", "Century Gothic", sans-serif;
    position: relative;
  }
  .card {
    position: absolute;
    top: 259px;
    width: 540px;
    height: 309px;
    overflow: hidden;
    box-shadow: 0 6px 18px rgba(0,0,0,0.45);
  }
  /* ---------- back ---------- */
  .card-back {
    left: 40px;
    background: linear-gradient(180deg, var(--card-black), var(--card-black-deep));
  }
  .card-back .ghost-name {
    position: absolute;
    left: 70px;
    top: 120px;
    font-size: 40px;
    line-height: 1.05;
    color: var(--ghost-grey);
    white-space: nowrap;
  }
  .card-back .intro {
    position: absolute;
    top: 24px;
    left: 30px;
    right: 30px;
    text-align: center;
    color: var(--text-green);
    font-size: 13.5px;
    line-height: 1.35;
  }
  .card-back .intro p + p { margin-top: 8px; }
  .service-list {
    position: absolute;
    list-style: none;
    color: var(--text-white);
    font-size: 14px;
    line-height: 1.28;
  }
  .service-list li { position: relative; padding-left: 16px; }
  .service-list li::before {
    content: "";
    position: absolute;
    left: 0; top: 5px;
    width: 8px; height: 8px;
    border-radius: 50%;
    background: var(--brand-green);
  }
  .service-list.col-one { left: 40px; top: 138px; }
  .service-list.col-two { left: 290px; top: 182px; }

  /* ---------- front ---------- */
  .card-front { left: 620px; background: var(--card-black); }
  .card-front .surface { position: absolute; inset: 0; }
  .brand {
    position: absolute;
    left: 190px;
    top: 42px;
    display: flex;
    align-items: flex-start;
    gap: 12px;
  }
  .brand-square {
    width: 26px; height: 26px;
    background: var(--brand-green);
    margin-top: 4px;
  }
  .brand-name {
    color: var(--brand-green);
    font-size: 25px;
    line-height: 1.15;
  }
  .person {
    position: absolute;
    left: 22px;
    top: 205px;
    color: var(--text-green);
  }
  .person .name { font-size: 16px; }
  .person .role { font-size: 13px; margin-top: 2px; }
  .contact-divider {
    position: absolute;
    left: 252px;
    top: 212px;
    width: 1px;
    height: 76px;
    background: var(--divider);
  }
  .contacts {
    position: absolute;
    left: 262px;
    top: 212px;
    list-style: none;
    color: var(--text-white);
    font-size: 14px;
    line-height: 1.55;
  }
  .contacts li { display: flex; align-items: center; gap: 6px; }
  .contacts svg { width: 12px; height: 12px; flex: none; }
</style>
</head>
<body>

<section class="card card-back" aria-label="Business card back">
  <div class="ghost-name">R&amp;T Cleanwave<br>Stripping, LLC</div>
  <div class="intro">
    <p>We bring the awesome power of Hydroveil Media Scouring equipment<br>to your location.</p>
    <p>Our services are environmentally safe and can remove any<br>coating from any surface.</p>
  </div>
  <ul class="service-list col-one">
    <li>Paint Stripping</li>
    <li>Auto Restoration</li>
    <li>Graffiti Removal</li>
    <li>Block Walls &amp; Stone</li>
    <li>Concrete</li>
  </ul>
  <ul class="service-list col-two">
    <li>Boats</li>
    <li>Iron Fences</li>
    <li>Tractors &amp; Trailers</li>
    <li>Pools &amp; Fountains</li>
    <li>Wood Restoration</li>
  </ul>
</section>

<section class="card card-front" aria-label="Business card front">
  <svg class="surface" width="540" height="309" viewBox="0 0 540 309" aria-hidden="true">
    <defs>
      <linearGradient id="paper" x1="0" y1="0" x2="0" y2="1">
        <stop offset="0" stop-color="var(--paper-white)"/>
        <stop offset="1" stop-color="var(--paper-grey)"/>
      </linearGradient>
    </defs>
    <polygon points="0,0 540,0 540,182 0,118" fill="url(#paper)"/>
    <polygon points="0,118 540,182 540,194 0,130" fill="var(--brand-green)"/>
  </svg>

  <div class="brand">
    <span class="brand-square"></span>
    <span class="brand-name">R&amp;T Cleanwave<br>Stripping, LLC</span>
  </div>

  <div class="person">
    <div class="name">Gordon Pelly, MBA, PMP</div>
    <div class="role">CEO/Founder</div>
  </div>

  <div class="contact-divider"></div>
  <ul class="contacts">
    <li>
      <svg viewBox="0 0 12 12" aria-label="Mobile"><rect x="3" y="0.5" width="6" height="11" rx="1" fill="none" stroke="var(--brand-green)" stroke-width="1.2"/><circle cx="6" cy="9.6" r="0.7" fill="var(--brand-green)"/></svg>
      915-382-6091
    </li>
    <li>
      <svg viewBox="0 0 12 12" aria-label="Office phone"><path d="M1 4 Q6 0 11 4 L9.5 5.5 L8 4.5 L8 3.5 Q6 3 4 3.5 L4 4.5 L2.5 5.5 Z" fill="var(--brand-green)"/><rect x="2.5" y="6" width="7" height="5" rx="1" fill="var(--brand-green)"/></svg>
      915-627-8853
    </li>
    <li>
      <svg viewBox="0 0 12 12" aria-label="Email"><rect x="0.5" y="2.5" width="11" height="7.5" fill="var(--brand-green)"/><polyline points="0.5,2.5 6,7 11.5,2.5" fill="none" stroke="var(--card-black)" stroke-width="1"/></svg>
      gpelly@rtcleanwavestripping.com
    </li>
  </ul>
</section>

</body>
</html>
```